Career Development Program Flyer

Freshen up the look and make it more promotional. We want our teachers to know about the career tracks we offer. This document spells it all out, but we want it to pop! This will be a tool to help attract new applicants who are interested in future growth as well as retain our current staff who are interested in promotional opportunities.

Target Market(s)

our current teachers looking for growth or applicants interviewing who are interested in future growth with the company

Font styles to use
Serif
Sans Serif

Colors
3277b5
0255a3
cedeed
fbee3f
85acd3
fbf289

Requirements
Must have
• -our logo (i can send a new version if needed)
• -the information in the document provided
• -for more information on our company visit www.sunfieldlearninghub.com

```html
<!DOCTYPE html>
<html lang="en">
<head>
<meta charset="utf-8">
<title>Career Growth Program – Sunfield Learning Hub</title>
<link rel="stylesheet" href="https://fonts.googleapis.com/css2?family=Lato:ital,wght@0,400;0,700;0,900;1,400;1,700&display=swap">
<style>
:root{
  --blue-deep:#0255a3;
  --blue:#3277b5;
  --blue-soft:#85acd3;
  --ice:#cedeed;
  --navy:#0c1e44;
  --navy-mid:#0f2a5a;
  --yellow:#fbee3f;
  --yellow-pale:#fbf289;
  --gold:#f3c21b;
  --orange:#f0a91c;
  --ink:#0e2553;
  --sage:#e3e8d8;
  --white:#ffffff;
}
*{box-sizing:border-box;margin:0;padding:0}
html,body{width:1000px;height:1200px;overflow:hidden;background:#6d6d6d}
body{font-family:"Lato",sans-serif;color:var(--ink)}
.flyer{position:relative;width:1000px;height:1200px;background:var(--white);overflow:hidden}

/* header */
.masthead{position:absolute;left:0;top:0;width:1000px;height:132px;
  background:linear-gradient(180deg,var(--blue) 0%,var(--blue-deep) 100%);color:var(--white)}
.brand{position:absolute;left:48px;top:40px;display:flex;align-items:center;gap:12px}
.brand-dot{width:46px;height:46px;border-radius:50%;background:var(--yellow)}
.brand-name{font-size:24px;font-weight:700;color:var(--white)}
.office{position:absolute;right:38px;top:48px;text-align:right}
.office-title{font-size:24px;font-weight:700;text-decoration:underline;text-underline-offset:4px;margin-right:14px}
.office-phone{font-size:21px;margin-top:6px;display:flex;align-items:center;gap:8px;justify-content:flex-end}

/* photo */
.hero-photo{position:absolute;left:0;top:132px;width:1000px;height:393px;
  background:linear-gradient(120deg,#c9a64a 0%,#b98f7a 25%,#c97ba6 50%,#b4a6c9 75%,#8f8aa8 100%)}

/* ribbon */
.ribbon{position:absolute;left:0;top:448px;width:1000px;height:140px}
.ribbon-text{position:absolute;left:169px;top:455px;width:659px;height:90px;text-align:center}
.ribbon-title{font-size:44px;font-weight:900;color:var(--ink);line-height:1;margin-top:10px}
.ribbon-sub{font-size:19px;color:var(--ink);margin-top:4px}

/* aide section */
.aides{position:absolute;left:0;top:583px;width:672px;height:219px;
  background:linear-gradient(90deg,var(--sage) 0%,#f2f4ec 60%,var(--white) 100%)}
.aides::after{content:"";position:absolute;left:8px;right:-6px;bottom:0;height:4px;background:var(--navy)}
.section-title{position:absolute;left:90px;top:14px;font-size:21px;font-weight:900;
  text-decoration:underline;text-underline-offset:4px;color:var(--ink);letter-spacing:-.2px}
.aide-cols{position:absolute;left:30px;top:68px;display:flex}
.aide-col{width:210px;padding:0 10px}
.aide-col+.aide-col{border-left:2px solid var(--ink)}
.aide-head{font-size:16px;font-weight:700;text-align:center;line-height:1.2;height:58px}
.aide-head .lite{font-weight:400}
.aide-head em{font-size:12px;font-style:italic;font-weight:700}
.diamond-list{list-style:none;font-size:14px;line-height:1.25}
.diamond-list li{position:relative;padding-left:18px;margin-bottom:8px}
.diamond-list li::before{content:"";position:absolute;left:2px;top:5px;width:7px;height:7px;
  background:var(--ink);transform:rotate(45deg)}

/* admin */
.admin{position:absolute;left:672px;top:583px;width:328px;height:227px;
  background:linear-gradient(180deg,var(--blue) 0%,var(--blue-deep) 100%);color:var(--white);padding:14px 0 0 28px}
.admin-title{font-size:21px;font-weight:700}
.admin-note{font-size:10px;font-style:italic;margin-top:-1px;padding-bottom:4px;
  border-bottom:2px solid var(--white);width:72px;white-space:nowrap}
.admin-list{list-style:none;margin-top:8px;font-size:17px}
.admin-list li{position:relative;padding-left:26px;line-height:27.5px}
.admin-list li::before{content:"";position:absolute;left:4px;top:11px;width:7px;height:7px;
  background:var(--white);transform:rotate(45deg)}
.admin-foot{font-size:8px;margin-top:7px;opacity:.9}

/* teachers */
.teachers{position:absolute;left:0;top:810px;width:1000px;height:300px;background:var(--navy);color:var(--white)}
.teachers-band{position:absolute;left:0;top:4px;width:1000px;height:48px}
.teachers-title{position:absolute;left:0;top:10px;width:1000px;text-align:center;font-size:27px;font-weight:900;letter-spacing:-.3px}
.teacher-cols{position:absolute;left:40px;top:70px;display:flex;gap:22px}
.teacher-col{width:216px}
.teacher-col:last-child{width:200px}
.teacher-head{font-size:19px;font-weight:700;line-height:1.1}
.teacher-role{font-size:15.5px;font-weight:400;border-bottom:1.5px solid var(--white);display:inline-block;padding-bottom:1px}
.dot-list{list-style:none;margin-top:12px;font-size:13px;line-height:1.22}
.dot-list li{position:relative;padding-left:21px;margin-bottom:12px}
.dot-list li::before{content:"";position:absolute;left:2px;top:3px;width:11px;height:11px;border-radius:50%;
  background:var(--white);box-shadow:inset -3px 0 0 var(--blue-soft)}

/* footer */
.footer{position:absolute;left:0;top:1110px;width:1000px;height:90px;
  background:linear-gradient(180deg,var(--blue) 0%,var(--blue-deep) 100%);color:var(--white)}
.address{position:absolute;left:30px;top:28px;display:flex;gap:12px;font-size:17px;line-height:1.25}
.more{position:absolute;right:32px;top:28px;text-align:right}
.more-title{font-size:17px;margin-right:34px}
.more-web{font-size:13.5px;display:flex;align-items:center;gap:6px;margin-top:2px}
</style>
</head>
<body>
<div class="flyer">

  <header class="masthead">
    <div class="brand">
      <span class="brand-dot"></span>
      <span class="brand-name">Sunfield Learning Hub</span>
    </div>
    <div class="office">
      <div class="office-title">Main Office:</div>
      <div class="office-phone">
        <svg width="22" height="22" viewBox="0 0 24 24" aria-hidden="true"><path d="M6.6 10.8a15 15 0 0 0 6.6 6.6l2.2-2.2a1 1 0 0 1 1-.25 11.4 11.4 0 0 0 3.6.6 1 1 0 0 1 1 1V20a1 1 0 0 1-1 1A17 17 0 0 1 3 4a1 1 0 0 1 1-1h3.5a1 1 0 0 1 1 1 11.4 11.4 0 0 0 .6 3.6 1 1 0 0 1-.25 1z" fill="#fff"/><path d="M15 3.5a6 6 0 0 1 5.5 5.5M15 6.5a3 3 0 0 1 2.5 2.5" stroke="#fff" stroke-width="1.6" fill="none"/></svg>
        (555) 310-2468
      </div>
    </div>
  </header>

  <div class="hero-photo" role="img" aria-label="Photo of a group of smiling preschool children on a yellow playground slide"></div>

  <svg class="ribbon" viewBox="0 0 1000 140" aria-hidden="true">
    <defs>
      <linearGradient id="ribbonFace" x1="0" y1="0" x2="1" y2="0">
        <stop offset="0" stop-color="#f7d21e"/>
        <stop offset=".5" stop-color="#fbee3f"/>
        <stop offset="1" stop-color="#f7d21e"/>
      </linearGradient>
    </defs>
    <polygon points="95,127 235,127 235,40 120,40 140,83" fill="var(--orange)"/>
    <polygon points="905,127 765,127 765,40 880,40 860,83" fill="var(--orange)"/>
    <polygon points="169,97 235,127 235,97" fill="#7a5a12"/>
    <polygon points="828,97 765,127 765,97" fill="#7a5a12"/>
    <rect x="169" y="7" width="659" height="90" fill="url(#ribbonFace)"/>
  </svg>
  <div class="ribbon-text">
    <div class="ribbon-title">Career Growth Program</div>
    <div class="ribbon-sub">Qualifications by Position</div>
  </div>

  <section class="aides">
    <h2 class="section-title">INFANT AND PRESCHOOL AIDE POSITIONS</h2>
    <div class="aide-cols">
      <div class="aide-col">
        <div class="aide-head">Infant or Preschool<br><span class="lite">Aide I</span></div>
        <ul class="diamond-list">
          <li>No ECE units</li>
          <li>Limited experience</li>
          <li>Training needed</li>
        </ul>
      </div>
      <div class="aide-col">
        <div class="aide-head">Infant or Preschool<br><span class="lite">Aide II</span></div>
        <ul class="diamond-list">
          <li>0-11 ECE units</li>
          <li>Experience in the field</li>
        </ul>
      </div>
      <div class="aide-col">
        <div class="aide-head">Infant or Preschool<br><span class="lite">Aide III,</span> <em>Extended Day Staff</em></div>
        <ul class="diamond-list">
          <li>0-11 ECE units</li>
          <li>Manages the classroom independently</li>
          <li>At least 3 years’ experience</li>
        </ul>
      </div>
    </div>
  </section>

  <aside class="admin">
    <h2 class="admin-title">Administration Positions</h2>
    <div class="admin-note">Not all positions are applicable at every site</div>
    <ul class="admin-list">
      <li>Office Assistant</li>
      <li>Office Administrator</li>
      <li>Assistant Director</li>
      <li>Director</li>
      <li>Senior Director</li>
    </ul>
    <p class="admin-foot">For a comprehensive list of job duties, please see the job descriptions.</p>
  </aside>

  <section class="teachers">
    <svg class="teachers-band" viewBox="0 0 1000 48" aria-hidden="true">
      <polygon points="104,48 128,0 855,0 836,48" fill="var(--blue-deep)"/>
    </svg>
    <h2 class="teachers-title">INFANT AND PRESCHOOL TEACHER POSITIONS</h2>
    <div class="teacher-cols">
      <div class="teacher-col">
        <div class="teacher-head">Infant or Preschool</div>
        <div class="teacher-role">Head Teacher, Jr. K Staff</div>
        <ul class="dot-list">
          <li>Minimum to qualify: AA + 12 ECE units with 2 years’ experience or 12 ECE units with 5 years’ experience</li>
          <li>Professional, enthusiastic and an influential role model to their peers, specifically those teaching in their age group.</li>
        </ul>
      </div>
      <div class="teacher-col">
        <div class="teacher-head">Infant or Preschool</div>
        <div class="teacher-role">Assistant Teacher</div>
        <ul class="dot-list">
          <li>Entry level teachers</li>
          <li>12 ECE units minimum</li>
        </ul>
      </div>
      <div class="teacher-col">
        <div class="teacher-head">Infant or Preschool</div>
        <div class="teacher-role">Master ECE Teacher</div>
        <ul class="dot-list">
          <li>Minimum to qualify: B.A. Degree in Child Development with 2 years’ experience or B.A. Degree in any subject with 12 ECE units and 7+ years’ experience</li>
          <li>Minimum to qualify: B.A. Degree in Child Development with 2 years’ experience or B.A. Degree in any subject with 12 ECE units and 7+ years’ experience</li>
        </ul>
      </div>
      <div class="teacher-col">
        <div class="teacher-head">Infant or Preschool</div>
        <div class="teacher-role">Teacher</div>
        <ul class="dot-list">
          <li>Entry level teachers</li>
          <li>12 ECE units minimum</li>
        </ul>
      </div>
    </div>
  </section>

  <footer class="footer">
    <div class="address">
      <svg width="24" height="30" viewBox="0 0 24 30" aria-hidden="true"><path d="M12 1a9 9 0 0 0-9 9c0 7 9 15 9 15s9-8 9-15a9 9 0 0 0-9-9z" fill="#fff"/><circle cx="12" cy="10" r="3.5" fill="var(--blue-deep)"/><ellipse cx="12" cy="27" rx="8" ry="2" fill="none" stroke="#fff" stroke-width="1.5"/></svg>
      <div>1450 Larkspur Avenue, Building C<br>Fairview, CA 90210</div>
    </div>
    <div class="more">
      <div class="more-title">For More Info:</div>
      <div class="more-web">
        <svg width="20" height="20" viewBox="0 0 20 20" aria-hidden="true"><g fill="none" stroke="#fff" stroke-width="1.3"><circle cx="10" cy="10" r="8.5"/><ellipse cx="10" cy="10" rx="3.8" ry="8.5"/><path d="M1.5 10h17M3 5.5h14M3 14.5h14"/></g></svg>
        www.sunfieldlearninghub.com
      </div>
    </div>
  </footer>

</div>
</body>
</html>
```